Baby Girl Nora Birth Announcement for Dec 1st 2020

Using an existing photo from an artist, build a 2 sided card with messaging and details on opposite side.

Style: fun, timeless, elegant, vibrant
Side 1:
Text "Welcome Nora".
Use file called FRONT BACKGROUND - Welcome Nora.
Consider 2 fonts, consider 2 colors of words. use provided image and monochromatic image of a heart
Side 2 content to be fit:
"Welcome to our little ray of light!"
"Nora Jade Ruth Pelkey"
Date of birth ---/--/----
Time of birth
Weight
Length
"Loving and Proud Parents : Greta Pelkey - Ter Hoorwijk & Daniel Pelkey"
Amazing and Wonderful God Parents : "Leimomi Kahue & Bastien De Kerckhove" + "Mina Ling Ashcombe & Grant Ashcombe "

Target Market(s)

Family and friends.
International audience (european/asian/american).
Urban, up market,

Requirements
Must have
• Use file called FRONT BACKGROUND - Welcome Nora on the front
Nice to have
• Consider 2 fonts, consider 2 colors of words. use provided image and monochromatic image of a heart

```html
<!DOCTYPE html>
<html lang="en">
<head>
<meta charset="utf-8">
<title>Welcome Nora – Birth Announcement</title>
<link rel="stylesheet" href="https://fonts.googleapis.com/css2?family=Great+Vibes&family=Libre+Baskerville:wght@400&family=Cormorant+Garamond:wght@400;500&display=swap">
<style>
  :root {
    --backdrop: #c6b199;
    --paper: #ffffff;
    --gold: #b8963f;
    --gold-deep: #a57f1c;
    --ink: #111111;
    --grey: #6e6e6e;
    --rule: #555555;
  }
  * { margin: 0; padding: 0; box-sizing: border-box; }
  html, body { width: 1200px; height: 1200px; overflow: hidden; }
  body { background: var(--backdrop); position: relative; font-family: "Libre Baskerville", Georgia, serif; }

  .card {
    position: absolute;
    left: 232px;
    width: 738px;
    height: 493px;
    background: var(--paper);
    border: 1px solid #b9b9b9;
    overflow: hidden;
  }
  .card--front { top: 101px; }
  .card--back { top: 611px; }

  /* Front */
  .front-photo {
    position: absolute; inset: 0;
    background:
      radial-gradient(circle at 88% 45%, rgba(255,250,225,1) 0, rgba(255,240,190,0.85) 12%, rgba(255,230,160,0) 32%),
      radial-gradient(ellipse at 18% 60%, rgba(90,150,200,0.75) 0, rgba(90,150,200,0) 40%),
      linear-gradient(180deg, #ffffff 0%, #f3f6f8 24%, #dfe7e2 42%, #a9b77c 55%, #c9c7a8 66%, #cfdde6 78%, #a9c3d6 100%);
  }
  .welcome-title {
    position: absolute; left: 0; top: 0;
    width: 738px; height: 240px;
    overflow: visible;
  }
  .welcome-label {
    font-family: "Cormorant Garamond", Georgia, serif;
    font-size: 22px;
    letter-spacing: 17px;
    fill: var(--grey);
  }
  .welcome-name {
    font-family: "Great Vibes", cursive;
    font-size: 150px;
    fill: var(--gold);
  }

  /* Back */
  .heart-shower {
    position: absolute; left: 0; top: 0;
    width: 100%; height: 225px;
    background: linear-gradient(180deg, rgba(184,150,63,0.28) 0%, rgba(184,150,63,0.14) 55%, rgba(184,150,63,0) 100%);
  }
  .greeting {
    position: absolute; left: 0; right: 0; top: 175px;
    text-align: center;
    font-size: 14px;
    letter-spacing: 5px;
    color: var(--ink);
  }
  .full-name {
    position: absolute; left: 0; top: 190px;
    width: 736px; height: 80px;
  }
  .full-name text {
    font-family: "Great Vibes", cursive;
    font-size: 52px;
    fill: var(--gold-deep);
  }
  .birth-details {
    position: absolute; left: 182px; top: 276px;
    display: flex;
    font-family: "Cormorant Garamond", Georgia, serif;
    font-weight: 500;
    font-size: 13px;
    color: var(--ink);
    white-space: nowrap;
  }
  .birth-details span { display: block; height: 25px; padding: 4px 4px 0; }
  .birth-details span + span { border-left: 1px solid var(--rule); }
  .detail-date { width: 124px; }
  .detail-time { width: 128px; }
  .detail-weight { width: 90px; }
  .detail-length { width: 80px; }
  .divider {
    position: absolute; left: 120px; top: 320px;
    width: 497px; height: 1px; background: var(--rule);
  }
  .credits {
    position: absolute; left: 0; right: 0; top: 338px;
    text-align: center;
    font-size: 10px;
    letter-spacing: 2.6px;
    line-height: 14px;
    color: var(--ink);
  }
  .credits h2 {
    font-weight: 400;
    font-size: 10px;
    color: var(--gold-deep);
  }
  .credits p + h2 { margin-top: 13px; }
</style>
</head>
<body>
  <section class="card card--front">
    <div class="front-photo" role="img" aria-label="Sunlit photograph of a glittering unicorn-costumed toy figure with small animal figures on an icy surface"></div>
    <svg class="welcome-title" viewBox="0 0 738 240" aria-label="Welcome Nora">
      <text class="welcome-name" x="112" y="182">Nora</text>
      <text class="welcome-label" x="32" y="87">WELCOME</text>
    </svg>
  </section>

  <section class="card card--back">
    <div class="heart-shower" role="img" aria-label="Scattered gold hearts falling from the top edge"></div>
    <p class="greeting">Welcome to our little ray of light!</p>
    <svg class="full-name" viewBox="0 0 736 80" aria-label="Nora Jade Ruth Pelkey">
      <text x="368" y="62" text-anchor="middle">Nora Jade Ruth Pelkey</text>
    </svg>
    <div class="birth-details">
      <span class="detail-date">Date of birth ---/--/----</span>
      <span class="detail-time">Time of birth</span>
      <span class="detail-weight">Weight</span>
      <span class="detail-length">Length</span>
    </div>
    <div class="divider"></div>
    <div class="credits">
      <h2>Loving and Proud Parents</h2>
      <p>Greta Pelkey - Ter Hoorwijk &amp; Daniel Pelkey</p>
      <h2>Amazing and Wonderful God Parents</h2>
      <p>Leimomi Kahue &amp; Bastien De Kerckhove</p>
      <p>Mina Ling Ashcombe &amp; Grant Ashcombe</p>
    </div>
  </section>
</body>
</html>
```